My business name is Rosalind Mae Design
I wish for a flower or flowers close up in pinks or purple
With my business Name on the front and all rest of the details on the back
I make artificial flower designs , I also make acrylic water designs ,and do my own art work ,I work from home ,

Target Market(s)

Every day people new homes etc

Industry/Entity Type

Business

Font styles to use
Script

Colors
e664a6
b667aa
6b449b

```html
<!DOCTYPE html>
<html lang="en">
<head>
<meta charset="utf-8">
<title>Rosalind Mae Design – Business Cards</title>
<link rel="stylesheet" href="https://fonts.googleapis.com/css2?family=Cormorant+SC:wght@600&family=Cormorant+Garamond:wght@500&family=Courgette&family=Open+Sans:wght@400&display=swap">
<style>
  :root {
    --pink-bright: #e664a6;
    --pink-deep: #c2278a;
    --pink-soft: #f4a6cf;
    --mauve: #b667aa;
    --purple: #6b449b;
    --purple-dark: #4a2668;
    --white: #ffffff;
    --backdrop: #efe9ee;
  }
  * { margin: 0; padding: 0; box-sizing: border-box; }
  html, body {
    width: 1200px; height: 1000px; overflow: hidden;
    background: var(--backdrop);
  }
  .canvas { position: relative; width: 1200px; height: 1000px; }

  .card {
    position: absolute;
    width: 560px; height: 320px;
    border-radius: 4px;
    overflow: hidden;
    box-shadow: 0 10px 28px rgba(74, 38, 104, 0.25);
  }
  .card--contact { left: 70px; top: 120px; }
  .card--brand { left: 570px; top: 560px; }

  .card__floral {
    position: absolute; inset: 0;
    background:
      radial-gradient(ellipse at 45% 55%, var(--pink-soft) 0%, transparent 55%),
      radial-gradient(circle at 85% 20%, var(--pink-bright) 0%, transparent 45%),
      radial-gradient(circle at 10% 85%, var(--pink-bright) 0%, transparent 40%),
      linear-gradient(135deg, var(--pink-deep) 0%, var(--pink-bright) 50%, var(--pink-deep) 100%);
  }

  .card__band {
    position: absolute; left: 0; right: 0; bottom: 0;
    height: 56px;
    background: linear-gradient(180deg, var(--purple) 0%, var(--purple-dark) 100%);
    display: flex; align-items: center; justify-content: center;
  }
  .card__tagline {
    font-family: "Courgette", cursive;
    font-size: 19px;
    color: var(--white);
    letter-spacing: 0.5px;
  }

  /* Contact side */
  .mark {
    position: absolute; left: 40px; top: 78px;
    width: 150px;
    display: flex; flex-direction: column; align-items: center; gap: 12px;
  }
  .mark__dot {
    width: 54px; height: 54px; border-radius: 50%;
    background: var(--mauve);
  }
  .mark__name {
    font-family: "Cormorant Garamond", serif;
    font-weight: 500;
    font-size: 22px;
    line-height: 1.1;
    color: var(--white);
    text-align: center;
  }
  .divider {
    position: absolute; left: 222px; top: 52px;
    width: 1px; height: 170px;
    background: rgba(255, 255, 255, 0.75);
  }
  .details { position: absolute; left: 248px; top: 48px; right: 20px; }
  .details__name {
    font-family: "Cormorant SC", serif;
    font-weight: 600;
    font-size: 28px;
    color: var(--white);
    margin-bottom: 16px;
    letter-spacing: 0.5px;
  }
  .details__list { list-style: none; }
  .details__item {
    display: flex; align-items: center; gap: 10px;
    font-family: "Open Sans", sans-serif;
    font-size: 13px;
    color: var(--white);
    margin-bottom: 12px;
  }
  .details__icon { width: 14px; height: 14px; flex: none; }

  /* Brand side */
  .brand {
    position: absolute; left: 40px; right: 30px; top: 0; bottom: 56px;
    display: flex; align-items: center; gap: 24px;
  }
  .brand__dot {
    width: 92px; height: 92px; border-radius: 50%;
    background: var(--mauve); flex: none;
  }
  .brand__name {
    font-family: "Cormorant Garamond", serif;
    font-weight: 500;
    font-size: 46px;
    color: var(--white);
    line-height: 1.05;
  }
</style>
</head>
<body>
<main class="canvas">

  <section class="card card--contact">
    <div class="card__floral" role="img" aria-label="Close-up photograph of soft pink phlox flowers"></div>

    <div class="mark">
      <span class="mark__dot"></span>
      <span class="mark__name">Rosalind Mae Design</span>
    </div>

    <span class="divider"></span>

    <div class="details">
      <h2 class="details__name">Rosalind Mae Ashby</h2>
      <ul class="details__list">
        <li class="details__item">
          <svg class="details__icon" viewBox="0 0 16 16" fill="#ffffff"><path d="M8 1a5 5 0 0 0-5 5c0 4 5 9 5 9s5-5 5-9a5 5 0 0 0-5-5zm0 7a2 2 0 1 1 0-4 2 2 0 0 1 0 4z"/></svg>
          Based in the small town of Willowbrook
        </li>
        <li class="details__item">
          <svg class="details__icon" viewBox="0 0 16 16" fill="#ffffff"><path d="M4 1l2.5 3-1.5 2c1 2 3 4 5 5l2-1.5 3 2.5-1.5 2.5C8 15 1 8 1.5 2.5z"/></svg>
          0400 555 019
        </li>
        <li class="details__item">
          <svg class="details__icon" viewBox="0 0 16 16" fill="none" stroke="#ffffff" stroke-width="1.5"><rect x="1.5" y="3.5" width="13" height="9"/><path d="M1.5 3.5l6.5 5 6.5-5"/></svg>
          hello@rosalindmae.com
        </li>
        <li class="details__item">
          <svg class="details__icon" viewBox="0 0 16 16" fill="none" stroke="#ffffff" stroke-width="1.3"><circle cx="8" cy="8" r="6.5"/><ellipse cx="8" cy="8" rx="3" ry="6.5"/><path d="M1.5 8h13"/></svg>
          rosalindmaedesign.example.com
        </li>
      </ul>
    </div>

    <div class="card__band">
      <p class="card__tagline">Made for the house to become a home.</p>
    </div>
  </section>

  <section class="card card--brand">
    <div class="card__floral" role="img" aria-label="Close-up photograph of soft pink phlox flowers"></div>

    <div class="brand">
      <span class="brand__dot"></span>
      <h1 class="brand__name">Rosalind Mae Design</h1>
    </div>

    <div class="card__band">
      <p class="card__tagline">Paintings, Homemade Arts and Crafts.</p>
    </div>
  </section>

</main>
</body>
</html>
```